Corvane Holdings , new business card design

investment firm with corporate clients . need double sided business card , vertical and horizontal options ,logo must be clear. prefer pantone colors only and sharp design. website also www.corvane-example.ae

Khalid Bin Rashed
Managing Director
Tel. +971 4 000 3829
Mobile +971 50 000 4172
khalid@corvane-example.ae
Palm Crest Tower, officw 18-B07, Qasr Gardens, Dubai

Contact Information for Business Card

Khalid Bin Rashed
Managing Director

Font styles to use
Serif

Colors

Designer to choose colors to be used in the design.

```html
<!DOCTYPE html>
<html lang="en">
<head>
<meta charset="utf-8">
<title>Corvane Holdings – Business Card</title>
<link rel="stylesheet" href="https://fonts.googleapis.com/css2?family=Tinos:wght@400;700&display=swap">
<style>
  :root{
    --stage:#c9c9cb;
    --white:#ffffff;
    --slate:#808084;
    --silver:#c4c4c6;
    --band-light:#aaaaae;
    --navy:#00205b;
    --azure:#1a82f0;
    --ink:#141414;
  }
  *{margin:0;padding:0;box-sizing:border-box}
  html,body{width:1200px;height:1000px;overflow:hidden}
  body{background:var(--stage);position:relative;font-family:"Tinos",serif}
  .card{position:absolute;overflow:hidden}
  .card svg.card-shapes{position:absolute;left:0;top:0}
  .card-front{left:72px;top:93px;width:712px;height:406px;background:var(--white)}
  .card-back{left:438px;top:557px;width:666px;height:380px;background:var(--silver)}

  .brand-name{position:absolute;font-family:"Tinos",serif;font-weight:400;color:var(--ink);
    text-align:center;text-transform:uppercase;line-height:1.05}
  .card-front .brand-name{left:40px;top:170px;width:262px;font-size:30px;letter-spacing:9px}
  .card-back .brand-name{left:132px;top:100px;width:402px;font-size:46px;letter-spacing:14px}

  .contact{position:absolute;right:42px;text-align:right;font-weight:700;
    color:var(--azure);font-size:17px;line-height:20px;white-space:nowrap}
  .contact-name{top:78px;text-transform:uppercase}
  .contact-name .role{display:block}
  .contact-address{top:149px;line-height:22px}
  .contact-phone{top:222px}
  .contact-email{top:303px}
</style>
</head>
<body>

<section class="card card-front" aria-label="Business card front">
  <svg class="card-shapes" width="712" height="406" viewBox="0 0 712 406" aria-hidden="true">
    <defs>
      <linearGradient id="strip-shade" x1="0" y1="0" x2="1" y2="0">
        <stop offset="0" stop-color="#f4f4f5"/>
        <stop offset="1" stop-color="#c9c9cc"/>
      </linearGradient>
    </defs>
    <rect class="edge-bar" x="0" y="62" width="25" height="282" fill="var(--navy)"/>
    <polygon class="divider-strip" points="283,0 324,0 443,406 383,406" fill="url(#strip-shade)"/>
    <polygon class="info-panel" points="324,0 712,0 712,406 443,406" fill="var(--slate)"/>

    <!-- icon tabs -->
    <g class="tab tab-person">
      <polygon points="301,72 362,72 369,126 316,126" fill="var(--navy)"/>
      <circle cx="331" cy="91" r="6" fill="#fff"/>
      <path d="M320 107 q11 -14 22 0 z" fill="#fff"/>
    </g>
    <g class="tab tab-pin">
      <polygon points="320,143 384,143 391,198 336,198" fill="var(--azure)"/>
      <path d="M355 161 a8 8 0 0 1 8 8 c0 6 -8 14 -8 14 s-8 -8 -8 -14 a8 8 0 0 1 8 -8z" fill="#fff"/>
      <circle cx="355" cy="169" r="3" fill="var(--azure)"/>
    </g>
    <g class="tab tab-phone">
      <polygon points="338,214 399,214 406,269 353,269" fill="var(--azure)"/>
      <path d="M362 232 l4 5 -3 4 c2 4 5 7 9 9 l4 -3 5 4 -3 5 c-10 -1 -18 -9 -20 -19z" fill="#fff"/>
    </g>
    <g class="tab tab-mail">
      <polygon points="356,286 418,286 425,340 370,340" fill="var(--azure)"/>
      <rect x="381" y="304" width="19" height="15" fill="#fff"/>
      <path d="M381 304 l9.5 9 9.5 -9" stroke="var(--azure)" stroke-width="2" fill="none"/>
    </g>

    <!-- accent rules -->
    <rect x="684" y="72" width="6" height="54" fill="var(--navy)"/>
    <rect x="684" y="143" width="6" height="55" fill="var(--azure)"/>
    <rect x="684" y="214" width="6" height="55" fill="var(--azure)"/>
    <rect x="684" y="286" width="6" height="54" fill="var(--azure)"/>
  </svg>

  <p class="brand-name">Corvane<br>Holdings</p>

  <p class="contact contact-name">Khalid Bin Rashed<span class="role">Managing Director</span></p>
  <p class="contact contact-address">Palm Crest Tower, Office 18-B07<br>Qasr Gardens, Dubai</p>
  <p class="contact contact-phone">+971 4 000 3829<br>+971 50 000 4172</p>
  <p class="contact contact-email">khalid@corvane-example.ae</p>
</section>

<section class="card card-back" aria-label="Business card back">
  <svg class="card-shapes" width="666" height="380" viewBox="0 0 666 380" aria-hidden="true">
    <rect class="base-band-light" x="0" y="303" width="666" height="27" fill="var(--band-light)"/>
    <rect class="base-band-dark" x="0" y="330" width="666" height="50" fill="var(--slate)"/>
    <polygon class="plinth" points="145,275 508,275 541,330 124,330" fill="var(--navy)"/>
  </svg>
  <p class="brand-name">Corvane<br>Holdings</p>
</section>

</body>
</html>
```